Business letterhead and powerpoint template

Hi, I have recently started using a new logo (found through PixelGrove) and would now like to use that logo for letterheads and powerpoint.

Attached is the logo and one version of a brochure I have recently used.

Industry/Entity Type

Business

```html
<!DOCTYPE html>
<html lang="en">
<head>
<meta charset="utf-8">
<title>Halden Capital Letterhead</title>
<link rel="stylesheet" href="https://fonts.googleapis.com/css2?family=Jost:wght@300;400;500&display=swap">
<style>
  :root {
    --backdrop: #e9e9ea;
    --paper: #ffffff;
    --ink: #4a4a4a;
    --ink-soft: #6d6d6d;
    --accent: #dc5038;
    --on-accent: #ffffff;
    --signature-fill: #e4e4e4;
  }
  * { box-sizing: border-box; margin: 0; padding: 0; }
  html, body {
    width: 1200px;
    height: 960px;
    overflow: hidden;
    background: var(--backdrop);
    font-family: "Jost", "Futura", sans-serif;
    color: var(--ink);
  }
  .letterhead {
    position: absolute;
    left: 282px;
    top: 30px;
    width: 636px;
    height: 900px;
    background: var(--paper);
    box-shadow: 0 8px 24px rgba(0,0,0,0.12);
    overflow: hidden;
  }
  .masthead {
    position: absolute;
    right: 48px;
    top: 46px;
    text-align: right;
  }
  .brand {
    display: flex;
    align-items: center;
    justify-content: flex-end;
    gap: 8px;
  }
  .brand-mark {
    width: 14px;
    height: 14px;
    background: var(--accent);
  }
  .brand-name {
    font-size: 26px;
    font-weight: 300;
    letter-spacing: 1px;
    color: var(--ink);
    line-height: 1;
  }
  .brand-sub {
    font-size: 8px;
    font-weight: 300;
    letter-spacing: 3px;
    color: var(--ink);
    margin-top: 3px;
    border-top: 1px solid var(--ink-soft);
    padding-top: 2px;
    display: inline-block;
  }
  .letter-date {
    font-size: 10px;
    font-weight: 300;
    color: var(--ink);
    margin-top: 16px;
  }
  .letter-body {
    position: absolute;
    left: 56px;
    top: 178px;
    width: 524px;
    font-size: 10px;
    font-weight: 300;
    line-height: 1.75;
    color: var(--ink-soft);
  }
  .salutation {
    color: var(--ink);
    font-weight: 400;
    margin-bottom: 18px;
  }
  .letter-body p { margin-bottom: 18px; text-align: left; }
  .closing {
    margin-top: 34px;
    color: var(--ink);
    font-weight: 400;
  }
  .signature {
    display: block;
    width: 120px;
    height: 22px;
    margin-top: 16px;
    background: var(--signature-fill);
  }
  .footer-band {
    position: absolute;
    left: 0;
    right: 0;
    bottom: 26px;
    height: 150px;
    background: var(--accent);
    color: var(--on-accent);
    padding: 28px 48px 0 48px;
    font-size: 10px;
    font-weight: 300;
    line-height: 1.9;
  }
  .footer-company {
    font-weight: 400;
    letter-spacing: 0.5px;
  }
  .contact-line {
    display: flex;
    align-items: center;
    gap: 18px;
  }
  .contact-item { display: inline-flex; align-items: center; gap: 6px; }
  .contact-item svg { width: 10px; height: 10px; fill: var(--on-accent); flex: none; }
</style>
</head>
<body>
  <main class="letterhead">
    <header class="masthead">
      <div class="brand">
        <span class="brand-mark"></span>
        <span class="brand-name">HALDEN</span>
      </div>
      <div class="brand-sub">CAPITAL</div>
      <div class="letter-date">Date : 02-Aug-14</div>
    </header>

    <section class="letter-body">
      <div class="salutation">Sir / Madam,</div>
      <p>Lorem ipsum dolor sit amet, consectetur adipiscing elit. Aenean vel placerat nisi, id vestibulum tellus. Proin ligula ipsum, ultrices sit amet justo id, ullamcorper porttitor augue. Nulla sed metus at nunc hendrerit porta. Sed egestas luctus cursus. Etiam commodo turpis nulla, sed ornare augue scelerisque vel. Aliquam erat volutpat. Nam scelerisque tincidunt risus a ultrices. Aenean imperdiet ante mi, vel dictum nibh tempor ac. Nunc auctor ut lorem vel vulputate. Praesent magna nunc, rhoncus ut ipsum eget, ullamcorper auctor nulla. Lorem ipsum dolor sit amet, consectetur adipiscing elit. Aenean vel placerat nisi, id vestibulum tellus. Proin ligula ipsum, ultrices sit amet justo id, ullamcorper porttitor augue. Nulla sed metus at nunc hendrerit porta. Sed egestas luctus cursus. Etiam commodo turpis nulla, sed ornare augue scelerisque vel. Aliquam erat volutpat. Nam scelerisque tincidunt risus a ultrices. Aenean imperdiet ante mi, vel dictum nibh tempor ac. Nunc auctor ut lorem vel vulputate. Praesent magna nunc, rhoncus ut ipsum eget, ullamcorper auctor nulla.</p>
      <p>Phasellus sem justo, suscipit ac laoreet id, tincidunt vel mauris. Nullam vulputate nisi ut sodales pulvinar. Vivamus convallis fringilla arcu non pellentesque. Aenean sed commodo neque. Duis volutpat eleifend sapien, et aliquam quam facilisis eu. Suspendisse viverra nec ligula quis scelerisque. Etiam nibh magna, aliquet vel aliquam quis, fermentum vestibulum nulla. Fusce pellentesque sem vel tristique pretium, risus elit sodales lectus, non aliquet nunc ipsum et nulla. Nunc sapien neque, pulvinar vel suscipit quis, laoreet non sapien. Phasellus sem justo, suscipit ac laoreet id, tincidunt vel mauris. Nullam vulputate nisi ut sodales pulvinar. Vivamus convallis fringilla arcu non pellentesque. Aenean sed commodo neque. Duis volutpat eleifend sapien, et aliquam quam facilisis eu. Suspendisse viverra nec ligula quis scelerisque. Etiam nibh magna, aliquet vel aliquam quis, fermentum vestibulum nulla. Fusce pellentesque sem vel tristique pretium, risus elit sodales lectus, non aliquet nunc ipsum et nulla. Nunc sapien neque, pulvinar vel suscipit quis, laoreet non sapien.</p>
      <div class="closing">Yours Sicerely</div>
      <span class="signature" role="img" aria-label="Handwritten signature of Halden Capital"></span>
    </section>

    <footer class="footer-band">
      <div class="footer-company">HALDEN CAPITAL</div>
      <div class="contact-item">
        <svg viewBox="0 0 10 10" aria-hidden="true"><path d="M5 0a3.5 3.5 0 0 0-3.5 3.5C1.5 6 5 10 5 10s3.5-4 3.5-6.5A3.5 3.5 0 0 0 5 0zm0 5a1.5 1.5 0 1 1 0-3 1.5 1.5 0 0 1 0 3z"/></svg>
        Level 8 Suite 14, 42 Harbour Lane, Northgate 2100 NSW, Australia
      </div>
      <div class="contact-line">
        <span class="contact-item">
          <svg viewBox="0 0 10 10" aria-hidden="true"><path d="M2 0h2l1 2.5-1.3 1a5.5 5.5 0 0 0 2.8 2.8l1-1.3L10 6v2a2 2 0 0 1-2 2A8 8 0 0 1 0 2a2 2 0 0 1 2-2z"/></svg>
          Phone: +61 (02) 5550 1234
        </span>
        <span class="contact-item">
          <svg viewBox="0 0 10 10" aria-hidden="true"><path d="M2 0h5v3H2zM0 3.5h10V8H8v2H2V8H0zm3 4v1.5h4V7.5z"/></svg>
          Fax: +61 (02) 5550 1235
        </span>
      </div>
      <div class="contact-item">
        <svg viewBox="0 0 10 10" aria-hidden="true"><path d="M5 0a5 5 0 1 0 0 10A5 5 0 0 0 5 0zm3.9 4.5H7A7 7 0 0 0 6.2 1.2a4 4 0 0 1 2.7 3.3zM5 1c.6.8 1 2.1 1 3.5H4C4 3.1 4.4 1.8 5 1zM3.8 1.2A7 7 0 0 0 3 4.5H1.1a4 4 0 0 1 2.7-3.3zM1.1 5.5H3a7 7 0 0 0 .8 3.3 4 4 0 0 1-2.7-3.3zM5 9c-.6-.8-1-2.1-1-3.5h2C6 6.9 5.6 8.2 5 9zm1.2-.2A7 7 0 0 0 7 5.5h1.9a4 4 0 0 1-2.7 3.3z"/></svg>
        www.haldencapital.com.au
      </div>
    </footer>
  </main>
</body>
</html>
```